Yoga Training Cerificate

Design a certificate of graduation from a Vinyasa Yoga Teacher Training Program.

The attached document is an example of the certificate I received as a graduate from a teacher training program. You can use it as a template.

Stylistically, what you design can be: visually enticing, professional, clean, and modern.

Please develop the "Tidal Lotus" logo and embed it within the certificate.

Please add a circular watermark behind the body of the certificate similar to the one found in the attachment; leave out the words Asana Guild because I am not associated with that organization.

The name of my school is "Tidal Lotus." And it was established in 2017, which you can include.

The certificate affirms that "' 'such-and-such' has successfully completed the Tidal Lotus modern vinyasa yoga training, completing two hundred hours of instruction in practice and theory. Within the power of our institution as a certifying agent we declare Such-and-such, now, a teacher competent to share the gift of yoga with the masses in a safe and effective."

My name -Dennis Halvorsen- should be at bottom with a faux-signature; position title: Tidal Lotus founder.

If you decide to include text on the fringe, like the example, it might include bars of text describing the maxims of the Tidal Lotus school reading:

This is Tidal Lotus
Breath is primary
Evolve the physical culture
Bring your unique expression to the practice
Take Breaks
Freestyle
Close your eyes
Feel deeper into your body
This is active meditation
This is moving meditation
This is modern meditation

And find a way to integrate Emojis like: Fire, Water, Prayer Hands, etc. as you see fit.

Generally, make the certificate look: official, clear and clean. You can base it from the example given. And try and create a graphic design that is more visually capturing then the example.

```html
<!DOCTYPE html>
<html lang="en">
<head>
<meta charset="utf-8">
<title>Tidal Lotus Certificate of Completion</title>
<link href="https://fonts.googleapis.com/css2?family=Quicksand:wght@400;500;700&family=Pinyon+Script&display=swap" rel="stylesheet">
<style>
  :root {
    --backdrop: #7a7a7a;
    --cream: #fcf8cb;
    --gold-light: #dfc56c;
    --gold-mid: #9a7433;
    --olive: #6b5425;
    --umber: #43280a;
    --logo-brown: #8b5f25;
    --maxim-brown: #9b7b3c;
    --ink: #4a3112;
    --rule: #6b5a3a;
    --white: #ffffff;
  }
  * { margin: 0; padding: 0; box-sizing: border-box; }
  html, body { width: 1200px; height: 1000px; overflow: hidden; }
  body { background: var(--backdrop); font-family: "Quicksand", sans-serif; position: relative; }

  .certificate {
    position: absolute; left: 166px; top: 193px;
    width: 868px; height: 613px;
    background: var(--cream);
    overflow: hidden;
  }
  .certificate__art { position: absolute; inset: 0; }

  .brand { position: absolute; left: 30px; top: 34px; width: 270px; height: 240px; color: var(--logo-brown); }
  .brand__name {
    font-weight: 700; font-size: 76px; line-height: 1.12;
    letter-spacing: -1px;
  }
  .brand__est {
    position: absolute; left: 282px; top: 96px;
    transform: rotate(90deg); transform-origin: left top;
    font-size: 28px; font-weight: 500; line-height: 30px; white-space: nowrap;
  }

  .maxims {
    position: absolute; left: 52px; top: 300px; width: 200px;
    list-style: none; text-align: center;
    color: var(--maxim-brown); font-size: 12.5px; line-height: 15px;
  }

  .title {
    position: absolute; right: 44px; top: 14px;
    color: var(--white); text-align: right;
  }
  .title__script { font-family: "Pinyon Script", cursive; font-size: 64px; font-weight: 400; line-height: 82px; }
  .title__sub { font-size: 17px; letter-spacing: 0.5px; line-height: 20px; margin-top: 10px; }

  .statement {
    position: absolute; right: 44px; width: 430px;
    text-align: right; color: var(--ink);
    font-size: 14.5px; line-height: 16.8px; font-weight: 500;
  }
  .statement--date { top: 177px; }
  .statement--body { top: 228px; }
  .statement--close { top: 442px; }
  .blank { display: inline-block; border-bottom: 1px solid var(--rule); height: 12px; vertical-align: baseline; }

  .rule { position: absolute; left: 394px; width: 430px; border-top: 1px solid var(--rule); }
  .rule--name { top: 373px; }
  .rule--role { top: 420px; }

  .signatory { position: absolute; left: 582px; top: 533px; width: 240px; text-align: center; color: var(--white); }
  .signatory__name { font-family: "Pinyon Script", cursive; font-size: 26px; line-height: 1.1; }
  .signatory__role { font-size: 13px; margin-top: 2px; }
</style>
</head>
<body>
  <main class="certificate">
    <svg class="certificate__art" width="868" height="613" viewBox="0 0 868 613">
      <defs>
        <radialGradient id="medallion-tone" cx="50%" cy="50%" r="50%">
          <stop offset="0" stop-color="#ffffff" stop-opacity="0.95"/>
          <stop offset="0.55" stop-color="#ffffff" stop-opacity="0.55"/>
          <stop offset="1" stop-color="#ffffff" stop-opacity="0.15"/>
        </radialGradient>
      </defs>

      <g class="watermarks">
        <circle role="img" aria-label="Lace mandala watermark behind the school maxims" cx="204" cy="297" r="188" fill="url(#medallion-tone)"/>
        <circle role="img" aria-label="Lace mandala watermark behind the certificate statement" cx="510" cy="338" r="102" fill="url(#medallion-tone)"/>
        <circle role="img" aria-label="Lace mandala watermark behind the certificate statement" cx="712" cy="358" r="132" fill="url(#medallion-tone)"/>
      </g>

      <g class="header-band">
        <path d="M405,150 Q440,40 500,0 L868,0 L868,150 Z" fill="var(--gold-light)"/>
        <path d="M455,150 Q510,35 594,0 L868,0 L868,150 Z" fill="var(--gold-mid)"/>
        <path d="M540,150 Q600,40 700,0 L868,0 L868,150 Z" fill="var(--olive)"/>
        <path d="M640,150 Q700,40 790,0 L868,0 L868,150 Z" fill="var(--umber)"/>
      </g>

      <g class="footer-band">
        <path d="M0,613 L0,557 Q90,515 194,513 L868,513 L868,613 Z" fill="var(--umber)"/>
        <path d="M0,613 L0,557 Q90,515 194,513 L409,513 Q300,525 229,613 Z" fill="var(--olive)"/>
        <path d="M0,613 L0,557 Q90,515 194,513 L279,513 Q190,530 134,613 Z" fill="var(--gold-mid)"/>
        <path d="M0,613 L0,557 Q90,515 194,513 Q110,540 49,613 Z" fill="var(--gold-light)"/>
      </g>
    </svg>

    <div class="brand">
      <div class="brand__name">Tidal<br>Lotus</div>
      <div class="brand__est">est 2017</div>
    </div>

    <ul class="maxims">
      <li>This is Tidal Lotus</li>
      <li>Breath is primary</li>
      <li>Evolve the physical culture</li>
      <li>Bring your unique expression</li>
      <li>to the practice</li>
      <li>Take Breaks</li>
      <li>Freestyle</li>
      <li>Close your eyes</li>
      <li>Feel deeper into your body</li>
      <li>This is active meditation</li>
      <li>This is moving meditation</li>
      <li>This is modern meditation</li>
    </ul>

    <header class="title">
      <h1 class="title__script">Certificate</h1>
      <p class="title__sub">OF COMPLETION</p>
    </header>

    <p class="statement statement--date">
      On this <span class="blank" style="width:88px;margin-left:8px"></span><br>
      day of <span class="blank" style="width:190px;margin-left:6px"></span> , <span class="blank" style="width:110px"></span>
    </p>

    <p class="statement statement--body">
      has successfully completed<br>
      the Tidal Lotus modern vinyasa yoga training,<br>
      completing two hundred hours<br>
      of instruction in practice and theory.<br>
      Within the power of our institution<br>
      as a certifying agent we declare
    </p>

    <div class="rule rule--name"></div>
    <div class="rule rule--role"></div>

    <p class="statement statement--close">
      now, a teacher competent<br>
      to share the gift of yoga<br>
      with the masses in a safe and effective.
    </p>

    <footer class="signatory">
      <p class="signatory__name">Dennis Halvorsen</p>
      <p class="signatory__role">Tidal Lotus Founder</p>
    </footer>
  </main>
</body>
</html>
```